I need a bag for flour with windows from the front ill attach some sample title is MAPLE KITCHEN BAKEMIX FLOUR
with color changing on the side stand up pouch I want to be able to put stickers ford different type of flour

Target Market(s)

retail store

Industry/Entity Type

flour retails

Font styles to use
Serif

Colors
0094D4
00A9DD
6FCCEA
C7EBF8
E9F6FB
00AB8E
00BBA5
67D7C9
C6EFE9
E9F9F6

Requirements
Must have
• creative
Nice to have
• I need a place so I can place the stickers of the flour
Should not have
• simple

```html
<!DOCTYPE html>
<html lang="en">
<head>
<meta charset="utf-8">
<title>Maple Kitchen Bakemix Flour – Stand-up Pouch</title>
<link rel="stylesheet" href="https://fonts.googleapis.com/css2?family=Archivo+Black&family=Libre+Baskerville:wght@700&family=Playfair+Display:wght@700;900&display=swap">
<style>
  :root {
    --backdrop: #bdbdbd;
    --mint-light: #d3f2ec;
    --mint: #a9e2d7;
    --teal-panel: #2fb79f;
    --teal-panel-dark: #1f9c86;
    --green-band: #0f7d64;
    --green-band-text: #0b4a3d;
    --charcoal: #1e3335;
    --ink: #232a2b;
    --white: #ffffff;
    --window-edge: #242b2c;
    --label-grey: #47565a;
    --arrow: #1d363b;
  }
  html, body {
    margin: 0;
    padding: 0;
    width: 983px;
    height: 1200px;
    overflow: hidden;
    background: var(--backdrop);
  }
  .board {
    display: block;
    width: 983px;
    height: 1200px;
  }
  .brand-panel-name {
    font-family: "Libre Baskerville", serif;
    font-weight: 700;
    fill: var(--ink);
  }
  .sticker-text {
    font-family: "Libre Baskerville", serif;
    font-weight: 700;
    fill: var(--ink);
    font-size: 19px;
  }
  .band-title {
    font-family: "Playfair Display", serif;
    font-weight: 900;
    fill: var(--white);
    font-size: 50px;
  }
  .band-subtitle {
    font-family: "Playfair Display", serif;
    font-weight: 900;
    fill: var(--green-band-text);
    font-size: 42px;
  }
  .weight-text {
    font-family: "Playfair Display", serif;
    font-weight: 900;
    fill: var(--ink);
    font-size: 32px;
  }
  .callout-label {
    font-family: "Archivo Black", sans-serif;
    fill: var(--label-grey);
    font-size: 40px;
  }
</style>
</head>
<body>
<svg class="board" viewBox="0 0 983 1200" xmlns="http://www.w3.org/2000/svg">
  <defs>
    <linearGradient id="pouchBody" x1="0" y1="0" x2="1" y2="1">
      <stop offset="0" stop-color="var(--mint)"/>
      <stop offset="0.5" stop-color="var(--mint-light)"/>
      <stop offset="1" stop-color="var(--mint)"/>
    </linearGradient>
    <linearGradient id="panelFill" x1="0" y1="0" x2="1" y2="1">
      <stop offset="0" stop-color="var(--teal-panel-dark)"/>
      <stop offset="1" stop-color="var(--teal-panel)"/>
    </linearGradient>
    <linearGradient id="sceneFill" x1="0" y1="0" x2="0" y2="1">
      <stop offset="0" stop-color="#bfe8e0" stop-opacity="0.2"/>
      <stop offset="0.6" stop-color="#8fcfc3" stop-opacity="0.45"/>
      <stop offset="1" stop-color="#bfe8e0" stop-opacity="0"/>
    </linearGradient>
    <linearGradient id="wheatFill" x1="0" y1="0" x2="0" y2="1">
      <stop offset="0" stop-color="#5f7f7b" stop-opacity="0.35"/>
      <stop offset="1" stop-color="#5f7f7b" stop-opacity="0.05"/>
    </linearGradient>
    <linearGradient id="windowFill" x1="0" y1="0" x2="0" y2="1">
      <stop offset="0" stop-color="#f4f4f4"/>
      <stop offset="1" stop-color="#ffffff"/>
    </linearGradient>
  </defs>

  <!-- Stand-up pouch, flat front -->
  <g class="pouch" transform="translate(330 226)">
    <rect class="pouch-body" x="0" y="0" width="530" height="815" fill="url(#pouchBody)"/>

    <!-- farm scene decoration -->
    <rect class="farm-scene" role="img" aria-label="Faint sketched farmhouse and mill scene" x="30" y="70" width="290" height="330" rx="6" fill="url(#sceneFill)"/>
    <!-- wheat decoration -->
    <rect class="wheat-sprig" role="img" aria-label="Sketched ears of wheat" x="18" y="205" width="180" height="215" rx="8" fill="url(#wheatFill)"/>

    <!-- quality badge -->
    <circle class="quality-badge" cx="72" cy="50" r="44" fill="var(--charcoal)" opacity="0.85"/>

    <!-- brand panel -->
    <g class="brand-panel">
      <rect x="310" y="0" width="220" height="262" fill="url(#panelFill)"/>
      <rect x="310" y="262" width="220" height="4" fill="var(--charcoal)"/>
      <text class="brand-panel-name" x="420" y="128" text-anchor="middle" font-size="26">MAPLE</text>
      <text class="brand-panel-name" x="420" y="164" text-anchor="middle" font-size="26">KITCHEN</text>
    </g>

    <!-- product window with sticker tab -->
    <g class="window">
      <path d="M74 557 C 74 430, 150 370, 290 362 C 420 356, 500 440, 506 557 Z" fill="url(#windowFill)"/>
      <path d="M300 362 C 420 360, 502 440, 510 557" fill="none" stroke="var(--window-edge)" stroke-width="6"/>
    </g>
    <g class="sticker">
      <path d="M150 280 H366 A12 12 0 0 1 378 292 V352 C 378 362, 370 366, 355 368 L 300 375 L 140 385 V292 A12 12 0 0 1 150 280 Z" fill="#f3f3f3"/>
      <text class="sticker-text" x="258" y="320" text-anchor="middle">WHOLE WHEAT</text>
      <text class="sticker-text" x="258" y="348" text-anchor="middle">FLOUR</text>
    </g>

    <!-- title band -->
    <g class="title-band">
      <rect x="0" y="557" width="530" height="125" fill="var(--green-band)"/>
      <rect x="0" y="557" width="530" height="3" fill="var(--charcoal)"/>
      <text class="band-title" x="265" y="618" text-anchor="middle" textLength="470" lengthAdjust="spacingAndGlyphs">MAPLE KITCHEN</text>
      <text class="band-subtitle" x="265" y="668" text-anchor="middle" textLength="440" lengthAdjust="spacingAndGlyphs">BAKEMIX FLOUR</text>
    </g>

    <!-- base -->
    <rect class="pouch-base" x="0" y="682" width="530" height="133" fill="var(--charcoal)"/>
    <rect x="0" y="682" width="530" height="3" fill="var(--mint)"/>
    <g class="weight-tab">
      <path d="M198 815 V762 A12 12 0 0 1 210 750 H350 A12 12 0 0 1 362 762 V815 Z" fill="var(--mint-light)"/>
      <text class="weight-text" x="280" y="800" text-anchor="middle">500g</text>
    </g>
  </g>

  <!-- sticker callout -->
  <g class="callout">
    <text class="callout-label" x="133" y="547">Sticker</text>
    <path d="M328 585 C 360 575, 380 598, 410 586 S 450 578, 470 584" fill="none" stroke="var(--arrow)" stroke-width="5" stroke-linecap="round"/>
    <path d="M462 570 L490 584 L462 598 Z" fill="var(--arrow)"/>
  </g>
</svg>
</body>
</html>
```